Nana Bee's needs your help creating a clean, simple, possibly vintage style label for a natural rem...

We need a label for a new product to be sold in local stores. It will be a bottle of fresh Elderberry Syrup which is a natural remedy for the flu, colds, and allergies. Our syrup is different from others in the market as it is fresh, needs to be refrigerated, and does not include preservatives, added sugar, alcohol, or anything artificial. We would like a label with easy to read text, with a clean or vintage look. We would like a 3 inch by 3 inch circle front label with mostly text, not too busy, and possibly a branch of elderberries may be included. We also need a 3 inch by 3 inch circle label for the back of the bottle with the nutrition facts, ingredients, dosage, and specific text. Both labels should be lighter in (background) color to stand out from the dark purple liquid inside. We're leaning towards black for the main text, but open to other ideas that are neutral and not too flashy.The final design should be clear, clean, making the main text visible if in a grocery store refrigerator. It should appeal to all, but mostly to natural minded mothers.
Target Market(s)
Natural minded mothers

```html
<!DOCTYPE html>
<html lang="en">
<head>
<meta charset="utf-8">
<title>Nana Bee's Elderberry Syrup – Labels</title>
<link rel="stylesheet" href="https://fonts.googleapis.com/css2?family=Old+Standard+TT:wght@400;700&family=Oswald:wght@500&family=Arimo:ital,wght@0,400;0,700;1,700&display=swap">
<style>
  :root {
    --page: #ffffff;
    --kraft-light: #f1e3d2;
    --kraft: #e6d2bc;
    --kraft-edge: #d9c2a8;
    --ink: #2b2624;
    --ink-soft: #4a423d;
    --berry: #3a2a33;
    --berry-leaf: #6b6a58;
  }
  * { box-sizing: border-box; margin: 0; padding: 0; }
  html, body { width: 1200px; height: 1200px; overflow: hidden; background: var(--page); }
  .canvas { position: relative; width: 1200px; height: 1200px; }

  .label {
    position: absolute; top: 330px; width: 540px; height: 540px; border-radius: 50%;
    background: radial-gradient(circle at 45% 40%, var(--kraft-light) 0%, var(--kraft) 70%, var(--kraft-edge) 100%);
    color: var(--ink);
    overflow: hidden;
  }
  .label--front { left: 40px; }
  .label--back { left: 620px; font-family: "Arimo", sans-serif; }
  .label svg { position: absolute; inset: 0; }

  .front-brand { font-family: "Old Standard TT", serif; font-size: 36px; font-weight: 400; fill: var(--ink); }
  .front-title { font-family: "Old Standard TT", serif; font-size: 52px; font-weight: 400; fill: var(--ink); }
  .front-sub { font-family: "Old Standard TT", serif; font-size: 36px; fill: var(--ink); letter-spacing: 4px; }
  .front-tag { font-family: "Oswald", sans-serif; font-size: 15px; fill: var(--ink); letter-spacing: 1px; }
  .ring-text { font-family: "Oswald", sans-serif; font-size: 25px; fill: var(--ink); letter-spacing: 0.5px; }

  .back-intro {
    position: absolute; top: 62px; left: 120px; width: 300px;
    text-align: center; font-size: 12.5px; line-height: 1.35; color: var(--ink);
  }
  .nutrition {
    position: absolute; top: 138px; left: 72px; width: 205px;
    border: 1.5px solid var(--ink); padding: 3px 5px; font-size: 8.5px; line-height: 1.3; color: var(--ink);
  }
  .nutrition h3 { font-size: 21px; font-weight: 700; line-height: 1; letter-spacing: -0.3px; }
  .nutrition .row { display: flex; justify-content: space-between; border-top: 0.8px solid var(--ink); }
  .nutrition .row.indent { padding-left: 10px; }
  .nutrition .row.thick { border-top-width: 4px; }
  .nutrition .right { justify-content: flex-end; }
  .nutrition .foot { border-top: 2px solid var(--ink); font-size: 6.5px; line-height: 1.2; padding-top: 1px; }

  .back-details {
    position: absolute; top: 138px; left: 285px; width: 190px;
    font-size: 11px; line-height: 1.3; color: var(--ink);
  }
  .back-details p + p { margin-top: 12px; }

  .disclaimer {
    position: absolute; top: 350px; left: 75px; width: 390px;
    font-size: 9px; line-height: 1.3; text-align: center; color: var(--ink);
  }
  .keep-cold {
    position: absolute; top: 392px; left: 0; width: 540px; text-align: center;
    font-size: 11.5px; font-weight: 700; font-style: italic; color: var(--ink-soft);
  }
  .maker {
    position: absolute; top: 416px; left: 0; width: 540px; text-align: center;
    font-size: 11px; font-weight: 700; color: var(--ink);
  }
  .maker .maker-name { font-family: "Old Standard TT", serif; font-size: 14px; color: #a12a2a; font-weight: 400; }
  .address {
    position: absolute; top: 440px; left: 0; width: 540px; text-align: center;
    font-size: 10.5px; font-weight: 700; color: var(--ink-soft);
  }
</style>
</head>
<body>
<main class="canvas">

  <section class="label label--front" aria-label="Front label">
    <svg viewBox="0 0 540 540" width="540" height="540">
      <defs>
        <path id="ring-top" d="M 95.3 416.6 A 228 228 0 1 1 444.7 416.6"/>
        <path id="ring-bottom" d="M 150 458 A 238 238 0 0 0 390 458"/>
      </defs>
      <text class="ring-text"><textPath href="#ring-top" startOffset="50%" text-anchor="middle" textLength="820" lengthAdjust="spacing">MADE WITH ORGANIC ELDERBERRIES &amp; SPICES &amp; LOCAL TEXAS RAW HONEY</textPath></text>
      <text class="ring-text"><textPath href="#ring-bottom" startOffset="50%" text-anchor="middle">NET WT 8 FL OZ</textPath></text>
      <circle cx="98" cy="437" r="4" fill="var(--ink)"/>
      <circle cx="442" cy="437" r="4" fill="var(--ink)"/>

      <text class="front-brand" x="270" y="170" text-anchor="middle">Nana Bee's</text>
      <text class="front-title" x="270" y="256" text-anchor="middle" textLength="370" lengthAdjust="spacingAndGlyphs">ELDERBERRY</text>
      <text class="front-sub" x="270" y="300" text-anchor="middle">SYRUP</text>
      <text class="front-tag" x="270" y="332" text-anchor="middle">IMMUNE BOOSTING</text>

      <g role="img" aria-label="Small drawing of an elderberry branch with berry clusters and leaves">
        <ellipse cx="270" cy="380" rx="58" ry="24" fill="var(--berry-leaf)" opacity="0.35"/>
        <ellipse cx="262" cy="388" rx="30" ry="16" fill="var(--berry)" opacity="0.75"/>
      </g>
    </svg>
  </section>

  <section class="label label--back" aria-label="Back label">
    <p class="back-intro">This delicious elderberry syrup boosts the immune system. It is a natural remedy for the flu, colds, and allergies.*</p>

    <div class="nutrition">
      <h3>Nutrition Facts</h3>
      <div>Serving Size 1 TBSP</div>
      <div>Servings Per Container 16</div>
      <div class="row thick"><span>Amount Per Serving</span></div>
      <div class="row"><b>Calories 20</b></div>
      <div class="row right"><span>% Daily Value*</span></div>
      <div class="row"><span><b>Total Fat</b> 0g</span><span>0%</span></div>
      <div class="row indent"><span>Saturated Fat 0g</span><span>0%</span></div>
      <div class="row indent"><span>Trans Fat 0g</span></div>
      <div class="row"><span><b>Sodium</b> 4mg</span><span>0%</span></div>
      <div class="row"><span><b>Total Carbohydrate</b> 5g</span><span>2%</span></div>
      <div class="row indent"><span>Dietary Fiber 0g</span><span>0%</span></div>
      <div class="row indent"><span>Sugars 4g</span></div>
      <div class="row"><span><b>Protein</b> 0g</span><span>0%</span></div>
      <div class="foot">*Percent Daily Values are based on a 2,000 calorie diet.</div>
    </div>

    <div class="back-details">
      <p>Ingredients: distilled water, local Texas raw honey, certified organic elderberries (sambucus nigra), certified organic ginger, certified organic cinnamon, certified organic cloves (immediately below or next to nutrition facts)</p>
      <p>For immune support: Adults 1 tbsp / Children 1 tsp once per day<br>For cold and flu treatment: Take one dose every 2-3 hours<br>DO NOT GIVE TO INFANTS UNDER 1 YEAR OF AGE</p>
    </div>

    <p class="disclaimer">*This statement has not been evaluated by the Food and Drug Administration. This product is not intended to diagnose, treat, cure, or prevent any disease.</p>
    <p class="keep-cold">KEEP REFRIGERATED</p>
    <p class="maker">Made with love by: <span class="maker-name">Nana Bee's</span></p>
    <p class="address">118 E Oak St Millbrook, Texas 75000</p>
  </section>

</main>
</body>
</html>
```